Hair Extension Website for my business store.

I need a e-commerce website for my store. Something similar to VORALA.com
Easy to update. May use WIX or Other platforms. I have my my own logo. It is gold. I’m looking for a website very similar to Vorala.com. The arrangement and all. Very easy to navigate. 5 pages. Over 100 products. Almost the same titles of the products.

Industry/Entity Type

Hair Care Product

Coding

Coded - Design and coding required

Number of Pages Required

5+ page

Font styles to use
Sans Serif

Colors
0255a3
fbed22

Requirements
Must have
• Something similar to Vorala.com

Prefered color purple and gold
Nice to have
• Similar to Vorala.com

Able to have many products.
Should not have
• I want all photos to lopk professional.

```html
<!DOCTYPE html>
<html lang="en">
<head>
<meta charset="utf-8">
<title>Aurelia Natural Hair – Shop</title>
<link href="https://fonts.googleapis.com/css2?family=Open+Sans:wght@400;600;700&family=Archivo+Black&display=swap" rel="stylesheet">
<style>
:root{
  --cyan:#1ec5f4;
  --orange:#ff5722;
  --red:#e5322b;
  --gold:#c9952c;
  --text:#444;
  --line:#e4e4e4;
  --side:#f5f5f5;
  --dark:#222b30;
  --badge-red:#f45c5c;
  --badge-yellow:#fec32b;
  --badge-blue:#1ea0f5;
}
*{margin:0;padding:0;box-sizing:border-box}
html,body{width:1200px;height:4229px;overflow:hidden;background:#fff}
body{position:relative;font-family:"Open Sans",Arial,sans-serif;color:var(--text)}
.a{position:absolute}
.topbar{left:0;top:0;width:1200px;height:40px;background:var(--cyan);color:#fff;font-size:14px;font-weight:700;letter-spacing:1px;line-height:40px;text-align:center}
.logo{left:190px;top:70px;width:105px;text-align:center;color:var(--gold);font-weight:700}
.logo .mark{width:40px;height:40px;border:3px solid var(--gold);border-radius:50%;margin:0 auto 4px}
.logo .name{font-size:22px;line-height:1}
.logo .sub{font-size:9px;letter-spacing:1px}
.toplinks{top:59px;font-size:12px;color:#333;display:flex;align-items:center;gap:6px}
.toplinks svg{width:12px;height:12px}
.sep{top:56px;width:1px;height:20px;background:var(--line)}
.search{left:433px;top:97px;width:500px;height:34px;border:2px solid #999;font-size:12px;color:#777;line-height:30px;padding-left:10px}
.searchbtn{left:932px;top:97px;width:53px;height:34px;background:var(--cyan)}
.cart{left:1036px;top:97px;width:42px;height:34px;background:var(--orange)}
.navbar{left:10px;top:182px;width:1180px;height:46px;border:1px solid #ddd}
.catsel{left:98px;top:186px;width:228px;height:38px;background:#f2f2f2;font-size:12px;line-height:38px;padding-left:12px;color:#333}
.nav{top:197px;font-size:13px;color:#333}
.hero{left:0;top:240px;width:1200px;height:525px;background:linear-gradient(100deg,#d79cb8 0%,#c47a9f 45%,#a55a82 100%)}
.model{left:905px;top:240px;width:295px;height:525px;background:linear-gradient(160deg,#2b1b1f,#4a2c30 60%,#6b3e45);border-radius:260px 0 0 260px}
.heroband{left:98px;top:350px;width:797px;height:101px;background:rgba(40,30,40,.55)}
.herotitle{left:0;width:1200px;text-align:center}
.shopnow{left:537px;top:570px;width:125px;height:36px;background:var(--cyan);color:#fff;font-size:14px;line-height:36px;text-align:center;letter-spacing:1px}
.dot{top:693px;width:11px;height:11px;border:1px solid #fff;border-radius:50%}
h2.sec{position:absolute;left:0;width:1200px;text-align:center;font-weight:400;font-size:40px;color:#111;line-height:1}
.orn{left:510px;width:180px;height:14px}
.sidebar{left:97px;top:946px;width:251px;height:1344px;background:var(--side)}
.sh{left:110px;font-size:17px;color:var(--orange);line-height:1}
.st{left:117px;font-size:11px;color:#444;line-height:1}
.chk{left:110px;font-size:11px;color:#444;display:flex;align-items:center;gap:8px;line-height:1}
.chk i{width:11px;height:11px;border:1px solid #aaa;background:#fff;display:block}
.stars{left:110px;font-size:13px;color:#ff9b00;letter-spacing:1px;line-height:1}
.stars b{color:#444;font-weight:400;font-size:11px;margin-left:8px}
.dealname{left:192px;font-size:12px;color:#333;line-height:1}
.dealprice{left:192px;font-size:14px;color:var(--red);line-height:1}
.card{background:#fff;box-shadow:0 0 8px rgba(0,0,0,.15)}
.ch{left:361px;width:729px;text-align:center;font-size:29px;font-weight:700;color:#111;line-height:1}
.pname{width:200px;text-align:center;font-size:14px;color:#222;line-height:1}
.price{width:200px;text-align:center;font-size:15px;color:var(--red);line-height:1}
.price s{color:#555;font-size:11px;margin-left:10px}
.btn{width:156px;height:37px;background:var(--cyan);color:#fff;font-size:11px;font-weight:700;letter-spacing:1px;text-align:center;line-height:37px}
.new{width:36px;height:36px;border-radius:50%;color:#fff;font-size:10px;text-align:center;line-height:36px}
.ph{background:linear-gradient(135deg,#3a3a3a,#111)}
.ph-blond{background:linear-gradient(135deg,#d7c9a8,#8a7b5c)}
.ph-brown{background:linear-gradient(135deg,#c39a6b,#4b3424)}
.ph-plum{background:linear-gradient(135deg,#7a1f45,#2a1020)}
.ph-pink{background:linear-gradient(135deg,#f6a8b6,#d06a7f)}
.ph-grey{background:linear-gradient(135deg,#b9b4c2,#5d5868)}
.promo{left:361px;top:1323px;width:729px;height:207px;background:var(--orange);color:#fff}
.ocard{background:#fff;border:1px solid #ddd;width:282px;height:300px;top:2470px}
.oname{left:17px;top:132px;width:250px;font-size:16px;color:#222;line-height:1.2;white-space:nowrap}
.oprice{left:17px;top:162px;font-size:18px;color:var(--red);line-height:1}
.oprice s{color:#555;font-size:12px;margin-left:12px}
.savebox{left:17px;top:196px;width:248px;height:32px;border:1px solid #bbb;font-size:13px;color:#555;line-height:30px;padding-left:10px}
.obtn{left:17px;top:244px;width:248px;height:33px;line-height:33px}
.news{left:0;top:2843px;width:1200px;height:297px;background:var(--dark)}
.foot-h{font-size:19px;color:var(--cyan);line-height:1}
.foot-l{font-size:11px;color:#666;line-height:1}
.feat{font-size:24px;font-weight:700;color:#222;letter-spacing:1px;line-height:1.3}
.fh{left:97px;font-size:17px;font-weight:700;color:#444;letter-spacing:.5px;line-height:1}
.fp{left:97px;width:1010px;font-size:10.5px;color:#888;line-height:22px}
.soc{top:3531px;width:26px;height:26px;border-radius:50%}
.storebtn{left:939px;width:150px;height:42px;background:#111;border-radius:6px;border:1px solid #555}
.pay{top:4076px;width:46px;height:28px;border:1px solid #ccc;border-radius:3px;background:#f2f2f2}
.bottom{left:0;top:4178px;width:1200px;height:51px;background:var(--orange);color:#fff;font-size:13px;letter-spacing:1px;text-align:center;line-height:51px}
</style>
</head>
<body>

<div class="a topbar">Aurelia Offer Zone Top Deals &amp; Discounts</div>

<div class="a logo">
  <div class="mark"></div>
  <div class="name">AURELIA</div>
  <div class="sub">NATURAL HAIR</div>
</div>

<div class="a toplinks" style="left:448px"><svg viewBox="0 0 12 12"><path d="M6 0a4 4 0 0 0-4 4c0 3 4 8 4 8s4-5 4-8a4 4 0 0 0-4-4z" fill="#ff5722"/></svg>Shop Locator</div>
<div class="a sep" style="left:560px"></div>
<div class="a toplinks" style="left:588px"><svg viewBox="0 0 12 12"><rect x="0" y="3" width="8" height="6" fill="#ff5722"/><rect x="8" y="5" width="4" height="4" fill="#ff5722"/></svg>Track Order</div>
<div class="a sep" style="left:688px"></div>
<div class="a toplinks" style="left:718px"><svg viewBox="0 0 12 12"><path d="M2 1l3 0 1 3-2 1a7 7 0 0 0 3 3l1-2 3 1 0 3c-6 0-10-4-10-9z" fill="#ff5722"/></svg>001 555 0142</div>
<div class="a sep" style="left:838px"></div>
<div class="a toplinks" style="left:874px"><svg viewBox="0 0 12 12"><rect x="2" y="5" width="8" height="7" fill="#ff5722"/><path d="M4 5V3a2 2 0 0 1 4 0v2" stroke="#ff5722" fill="none" stroke-width="1.5"/></svg>Sign In</div>
<div class="a sep" style="left:975px"></div>
<div class="a toplinks" style="left:1004px"><svg viewBox="0 0 12 12"><rect x="1" y="2" width="9" height="9" fill="none" stroke="#ff5722"/><path d="M5 8l6-6" stroke="#ff5722" stroke-width="2"/></svg>Sign Up</div>
<div class="a sep" style="left:1107px"></div>

<div class="a search">How can we help you today?</div>
<div class="a searchbtn"><svg class="a" style="left:20px;top:11px" width="13" height="13" viewBox="0 0 13 13"><circle cx="5" cy="5" r="3.5" stroke="#fff" stroke-width="2" fill="none"/><path d="M8 8l4 4" stroke="#fff" stroke-width="2"/></svg></div>
<div class="a cart"><svg class="a" style="left:12px;top:9px" width="18" height="16" viewBox="0 0 18 16"><path d="M0 1h3l2 9h10l2-7H4" stroke="#fff" stroke-width="2" fill="none"/><circle cx="6" cy="14" r="1.5" fill="#fff"/><circle cx="14" cy="14" r="1.5" fill="#fff"/></svg></div>

<div class="a navbar"></div>
<div class="a catsel">All Categories<span style="position:absolute;right:10px;font-size:9px">▼</span></div>
<div class="a nav" style="left:417px;color:var(--orange)">Home</div>
<div class="a nav" style="left:500px">About Us</div>
<div class="a nav" style="left:606px">Hair Weave ▾</div>
<div class="a nav" style="left:740px">Closure &amp; Frontal ▾</div>
<div class="a nav" style="left:916px">Pages ▾</div>
<div class="a nav" style="left:1016px">Contact</div>

<!-- hero banner -->
<div class="a hero" role="img" aria-label="Promotional banner artwork in pink and mauve with large stylised fashion lettering"></div>
<div class="a model" role="img" aria-label="Model with long dark wavy hair beside tropical leaves"></div>
<div class="a heroband"></div>
<div class="a herotitle" style="top:334px;left:-80px;font-size:30px;color:#222;line-height:1.1">We Bet You'll Love</div>
<div class="a herotitle" style="top:372px;font-family:'Archivo Black',sans-serif;font-size:56px;line-height:1;color:#fff">BIG <span style="color:#e8232f">DEAL</span></div>
<div class="a herotitle" style="top:480px;font-size:18px;color:#fff;letter-spacing:5px">Get Best Offer Upto <b style="font-size:32px;letter-spacing:1px">20%</b></div>
<div class="a shopnow">Shop Now</div>
<svg class="a" style="left:82px;top:495px" width="20" height="26" viewBox="0 0 20 26"><path d="M16 2L4 13l12 11" stroke="#fff" stroke-width="3" fill="none"/></svg>
<svg class="a" style="left:1098px;top:495px" width="20" height="26" viewBox="0 0 20 26"><path d="M4 2l12 11L4 24" stroke="#fff" stroke-width="3" fill="none"/></svg>
<div class="a dot" style="left:568px"></div>
<div class="a dot" style="left:583px"></div>
<div class="a dot" style="left:597px;background:#fff"></div>
<div class="a dot" style="left:612px"></div>

<h2 class="sec" style="top:838px">Our Top Products</h2>
<svg class="a orn" style="top:892px" viewBox="0 0 180 14"><line x1="0" y1="7" x2="70" y2="7" stroke="#999"/><line x1="110" y1="7" x2="180" y2="7" stroke="#999"/><path d="M72 7l6-6 6 6-6 6z" fill="#ff5722"/><path d="M84 7l6-6 6 6-6 6z" fill="#1ea0f5"/><path d="M96 7l6-6 6 6-6 6z" fill="#ff5722"/></svg>

<!-- sidebar -->
<div class="a sidebar"></div>
<div class="a sh" style="top:982px">Search Here..</div>
<div class="a" style="left:110px;top:1019px;width:186px;height:32px;background:#fff;font-size:10px;color:#888;line-height:32px;padding-left:9px">Product name...</div>
<div class="a" style="left:296px;top:1019px;width:39px;height:32px;background:var(--cyan)"><svg class="a" style="left:14px;top:10px" width="10" height="12" viewBox="0 0 10 12"><path d="M2 1l6 5-6 5" stroke="#fff" stroke-width="2" fill="none"/></svg></div>
<div class="a sh" style="top:1092px">Price range</div>
<div class="a st" style="left:110px;top:1126px">$50 &nbsp; - &nbsp; $6000</div>
<div class="a" style="left:117px;top:1155px;width:218px;height:4px;background:#ddd"></div>
<div class="a" style="left:117px;top:1155px;width:150px;height:4px;background:var(--cyan)"></div>
<div class="a" style="left:110px;top:1150px;width:14px;height:14px;border-radius:50%;background:var(--orange)"></div>
<div class="a" style="left:260px;top:1150px;width:14px;height:14px;border-radius:50%;background:var(--orange)"></div>

<div class="a sh" style="top:1207px">Discount</div>
<div class="a chk" style="top:1244px"><i></i>5% or More</div>
<div class="a chk" style="top:1270px"><i></i>10% or More</div>
<div class="a chk" style="top:1295px"><i></i>20% or More</div>
<div class="a chk" style="top:1321px"><i></i>30% or More</div>
<div class="a chk" style="top:1346px"><i></i>50% or More</div>
<div class="a chk" style="top:1372px"><i></i>60% or More</div>

<div class="a sh" style="top:1414px">Customer Review</div>
<div class="a stars" style="top:1451px">★★★★★<b>5.0</b></div>
<div class="a stars" style="top:1475px">★★★★☆<b>4.0</b></div>
<div class="a stars" style="top:1500px">★★★½☆<b>3.5</b></div>
<div class="a stars" style="top:1525px">★★★☆☆<b>3.0</b></div>
<div class="a stars" style="top:1549px">★★½☆☆<b>2.5</b></div>

<div class="a sh" style="top:1591px">Texture</div>
<div class="a chk" style="top:1628px"><i></i>Straight</div>
<div class="a chk" style="top:1654px"><i></i>Body Wave</div>
<div class="a chk" style="top:1679px"><i></i>Deep Wave</div>
<div class="a chk" style="top:1705px"><i></i>Loose Wave</div>
<div class="a chk" style="top:1731px"><i></i>Water Wave</div>
<div class="a chk" style="top:1756px"><i></i>Kinky Curly</div>
<div class="a chk" style="top:1782px"><i></i>Kinky Straight</div>
<div class="a chk" style="top:1808px"><i></i>Yaki</div>
<div class="a chk" style="top:1833px"><i></i>Jerry Curl</div>
<div class="a chk" style="top:1859px"><i></i>Spiral Curl</div>

<div class="a sh" style="top:1901px">Special Deals</div>
<div class="a dealname" style="top:1946px">Hair Weave</div>
<div class="a dealprice" style="top:1973px">$18.00</div>
<div class="a dealname" style="top:2013px">Closure &amp; Frontal</div>
<div class="a dealprice" style="top:2040px">$9.00</div>
<div class="a ph-brown" style="left:130px;top:2077px;width:39px;height:51px" role="img" aria-label="Hair product package"></div>
<div class="a dealname" style="top:2082px">Icenunew</div>
<div class="a dealprice" style="top:2109px">$15.00</div>
<div class="a dealname" style="top:2158px">Kyssissnew</div>
<div class="a dealprice" style="top:2185px">$525.00</div>
<div class="a dealname" style="top:2225px">Banicoonew</div>
<div class="a dealprice" style="top:2252px">$149.00</div>

<!-- Hair Weave -->
<div class="a card" style="left:361px;top:946px;width:729px;height:364px"></div>
<div class="a ch" style="top:973px">Hair Weave</div>
<div class="a ph" style="left:450px;top:1031px;width:90px;height:118px" role="img" aria-label="Straight black hair weave bundle"></div>
<div class="a ph" style="left:681px;top:1031px;width:90px;height:118px" role="img" aria-label="Deep wave black hair weave bundle"></div>
<div class="a new" style="left:558px;top:1033px;background:var(--badge-red)">New</div>
<div class="a new" style="left:788px;top:1033px;background:var(--badge-yellow)">New</div>
<div class="a new" style="left:1019px;top:1033px;background:var(--badge-blue)">New</div>
<div class="a pname" style="left:394px;top:1186px">Straight, 10in</div>
<div class="a price" style="left:394px;top:1216px">$149.00<s>$280.00</s></div>
<div class="a btn" style="left:417px;top:1246px">ADD TO CART</div>
<div class="a pname" style="left:626px;top:1186px">Deep Wave, 12in</div>
<div class="a price" style="left:626px;top:1216px">$200.00<s>$420.00</s></div>
<div class="a btn" style="left:648px;top:1246px">ADD TO CART</div>
<div class="a pname" style="left:855px;top:1088px">Body Wave, 14in</div>
<div class="a price" style="left:855px;top:1119px">$520.99<s>$600.99</s></div>
<div class="a btn" style="left:878px;top:1148px">ADD TO CART</div>

<div class="a promo">
  <div class="a" style="left:31px;top:62px;font-size:42px;font-weight:700;letter-spacing:3px;line-height:1">Pure Hair</div>
  <div class="a" style="left:31px;top:123px;font-size:15px;letter-spacing:1.5px">Enjoy our all hair Products</div>
  <div class="a" style="left:31px;top:160px;font-size:13px;letter-spacing:1px">Get Extra 10% Off</div>
  <div class="a" style="left:320px;top:80px;width:200px;text-align:center;font-size:26px;font-weight:700;color:#d0421a;transform:rotate(-72deg);letter-spacing:1px">Natural Hair</div>
</div>

<!-- Hair Extensions -->
<div class="a card" style="left:361px;top:1543px;width:729px;height:269px"></div>
<div class="a ch" style="top:1572px">Hair Extensions</div>
<div class="a new" style="left:558px;top:1632px;background:var(--badge-red)">New</div>
<div class="a new" style="left:788px;top:1632px;background:var(--badge-yellow)">New</div>
<div class="a new" style="left:1019px;top:1632px;background:var(--badge-blue)">New</div>
<div class="a pname" style="left:394px;top:1687px">Clip-In Set, 16in</div>
<div class="a price" style="left:394px;top:1717px">$78.00<s>$110.00</s></div>
<div class="a btn" style="left:417px;top:1747px">ADD TO CART</div>
<div class="a pname" style="left:626px;top:1687px">Tape-In Set, 18in</div>
<div class="a price" style="left:626px;top:1717px">$130.00<s>$150.00</s></div>
<div class="a btn" style="left:648px;top:1747px">ADD TO CART</div>
<div class="a pname" style="left:855px;top:1687px">Halo Piece, 20in</div>
<div class="a price" style="left:855px;top:1717px">$399.99<s>$500.00</s></div>
<div class="a btn" style="left:878px;top:1747px">ADD TO CART</div>

<!-- Accessories -->
<div class="a card" style="left:361px;top:1825px;width:729px;height:347px"></div>
<div class="a ch" style="top:1853px">Accessories</div>
<div class="a ph-blond" style="left:428px;top:1912px;width:132px;height:99px" role="img" aria-label="Blonde body wave hair bundle"></div>
<div class="a ph-brown" style="left:668px;top:1912px;width:113px;height:88px" role="img" aria-label="Brown ombre body wave hair bundle"></div>
<div class="a ph-plum" style="left:903px;top:1912px;width:105px;height:79px" role="img" aria-label="Burgundy body wave hair bundle"></div>
<div class="a new" style="left:788px;top:1913px;background:var(--badge-yellow)">New</div>
<div class="a new" style="left:1019px;top:1913px;background:var(--badge-blue)">New</div>
<div class="a pname" style="left:394px;top:2048px">Blonde Wave, 16in</div>
<div class="a price" style="left:394px;top:2078px">$15.00<s>$25.00</s></div>
<div class="a btn" style="left:417px;top:2108px">ADD TO CART</div>
<div class="a pname" style="left:626px;top:2035px">Ombre Wave, 18in</div>
<div class="a price" style="left:626px;top:2065px">$98.00<s>$120.00</s></div>
<div class="a btn" style="left:648px;top:2093px">ADD TO CART</div>
<div class="a pname" style="left:855px;top:2029px">Burgundy Wave, 20in</div>
<div class="a price" style="left:855px;top:2058px">$11.99<s>$15.00</s></div>
<div class="a btn" style="left:878px;top:2088px">ADD TO CART</div>

<!-- special offers -->
<h2 class="sec" style="top:2364px">Special Offers</h2>
<svg class="a orn" style="top:2417px" viewBox="0 0 180 14"><line x1="0" y1="7" x2="70" y2="7" stroke="#999"/><line x1="110" y1="7" x2="180" y2="7" stroke="#999"/><path d="M72 7l6-6 6 6-6 6z" fill="#ff5722"/><path d="M84 7l6-6 6 6-6 6z" fill="#1ea0f5"/><path d="M96 7l6-6 6 6-6 6z" fill="#ff5722"/></svg>

<div class="a ocard" style="left:157px">
  <div class="a ph-pink" style="left:75px;top:18px;width:132px;height:98px" role="img" aria-label="Pink body wave hair bundle"></div>
  <div class="a oname">Pink Body Wave, 14in</div>
  <div class="a oprice">$99.00<s>$200.00</s></div>
  <div class="a savebox">Save $20.00</div>
  <div class="a btn obtn">ADD TO CART</div>
</div>
<div class="a ocard" style="left:459px">
  <div class="a ph-grey" style="left:88px;top:18px;width:105px;height:98px" role="img" aria-label="Grey body wave hair bundle"></div>
  <div class="a oname">Grey Body Wave, 16in</div>
  <div class="a oprice">$69.00<s>$89.00</s></div>
  <div class="a savebox">Save $20.00</div>
  <div class="a btn obtn">ADD TO CART</div>
</div>
<div class="a ocard" style="left:761px">
  <div class="a ph-blond" style="left:88px;top:18px;width:105px;height:98px" role="img" aria-label="Platinum blonde body wave hair bundle"></div>
  <div class="a oname">Platinum Body Wave, 18in</div>
  <div class="a oprice">$187.00<s>$217.00</s></div>
  <div class="a savebox">Save $30.00</div>
  <div class="a btn obtn">ADD TO CART</div>
</div>
<svg class="a" style="left:97px;top:2607px" width="26" height="26" viewBox="0 0 26 26"><circle cx="13" cy="13" r="12" fill="none" stroke="#222" stroke-width="1.5"/><path d="M15 8l-5 5 5 5" stroke="#222" stroke-width="2" fill="none"/></svg>
<svg class="a" style="left:1074px;top:2607px" width="26" height="26" viewBox="0 0 26 26"><circle cx="13" cy="13" r="12" fill="none" stroke="#222" stroke-width="1.5"/><path d="M11 8l5 5-5 5" stroke="#222" stroke-width="2" fill="none"/></svg>

<!-- newsletter -->
<div class="a news">
  <div class="a" style="left:56px;top:54px;font-size:32px;font-weight:700;color:#fff;letter-spacing:.5px">Get your Hair Bundles delivered to your door</div>
  <div class="a" style="left:56px;top:107px;font-size:15px;color:#fff">Free Delivery on your first order!</div>
  <div class="a" style="left:56px;top:168px;width:532px;height:44px;background:#eee;font-size:14px;color:#777;line-height:44px;padding-left:12px">E-mail</div>
  <div class="a" style="left:594px;top:168px;width:130px;height:44px;background:var(--orange);color:#fff;font-size:15px;text-align:center;line-height:44px">Subscribe</div>
  <div class="a" style="left:816px;top:38px;width:354px;height:259px;background:linear-gradient(150deg,#3b4448,#7e8a8a 50%,#d8d0c4);border-radius:10px 10px 0 0" role="img" aria-label="Hand using a tablet showing a store map"></div>
</div>

<p class="a fp" style="top:3206px;font-size:13px;color:#555;line-height:25px">"AURELIA Natural Hair" Nemo enim ipsam voluptatem quia voluptas sit aspernatur aut odit aut fugit, sed quia consequuntur magni dolores eos qui ratione voluptatem sequi nesciunt.Sed ut perspiciatis unde omnis iste natus error sit voluptatem accusantium doloremque laudantium, totam rem aperiam, eaque ipsa quae ab illo inventore veritatis et quasi architecto beatae vitae dicta sunt explicabo.</p>
<div class="a" style="left:97px;top:3321px;width:1006px;height:1px;background:var(--line)"></div>

<svg class="a" style="left:152px;top:3370px" width="18" height="24" viewBox="0 0 18 24"><path d="M9 0a8 8 0 0 0-8 8c0 6 8 16 8 16s8-10 8-16a8 8 0 0 0-8-8z" fill="#ff5722"/><circle cx="9" cy="8" r="3" fill="#fff"/></svg>
<div class="a feat" style="left:213px;top:3349px">Track Your<br>Order</div>
<svg class="a" style="left:484px;top:3370px" width="24" height="24" viewBox="0 0 24 24"><path d="M20 10a8 8 0 0 0-15-3M4 14a8 8 0 0 0 15 3" stroke="#ff5722" stroke-width="3" fill="none"/><path d="M3 2v6h6M21 22v-6h-6" stroke="#ff5722" stroke-width="3" fill="none"/></svg>
<div class="a feat" style="left:548px;top:3349px">Free &amp; Easy<br>Returns</div>
<svg class="a" style="left:822px;top:3372px" width="20" height="20" viewBox="0 0 20 20"><path d="M3 3l14 14M17 3L3 17" stroke="#ff5722" stroke-width="4"/></svg>
<div class="a feat" style="left:883px;top:3349px">Online<br>cancellation</div>
<div class="a" style="left:97px;top:3442px;width:1006px;height:1px;background:var(--line)"></div>

<!-- footer columns -->
<div class="a foot-h" style="left:110px;top:3488px">Categories</div>
<div class="a foot-l" style="left:110px;top:3536px">Bundles</div>
<div class="a foot-l" style="left:110px;top:3566px">Closures</div>
<div class="a foot-l" style="left:110px;top:3597px">Frontals</div>
<div class="a foot-l" style="left:110px;top:3628px">Wigs</div>
<div class="a foot-l" style="left:110px;top:3659px">Clip-In Extensions</div>
<div class="a foot-l" style="left:110px;top:3689px">Ponytails</div>
<div class="a foot-l" style="left:307px;top:3536px">Shampoo &amp; Conditioner</div>
<div class="a foot-l" style="left:307px;top:3566px">Oils &amp; Serums</div>
<div class="a foot-l" style="left:307px;top:3597px">Edge Control</div>
<div class="a foot-l" style="left:307px;top:3628px">Combs &amp; Brushes</div>
<div class="a foot-l" style="left:307px;top:3659px">Personal Care</div>
<div class="a foot-l" style="left:307px;top:3689px">Wig Caps &amp; Tools</div>

<div class="a foot-h" style="left:529px;top:3488px">Quick Links</div>
<div class="a foot-l" style="left:529px;top:3536px">About Us</div>
<div class="a foot-l" style="left:529px;top:3566px">Contact Us</div>
<div class="a foot-l" style="left:529px;top:3597px">Help</div>
<div class="a foot-l" style="left:529px;top:3628px">Faqs</div>
<div class="a foot-l" style="left:529px;top:3659px">Terms of use</div>
<div class="a foot-l" style="left:529px;top:3689px">Privacy Policy</div>

<div class="a foot-h" style="left:726px;top:3488px">Get in Touch</div>
<div class="a foot-l" style="left:726px;top:3536px"><span style="color:var(--orange)">⬤</span>&nbsp;&nbsp; 48 Linden Row, Marlow</div>
<div class="a foot-l" style="left:726px;top:3566px"><span style="color:var(--orange)">▯</span>&nbsp;&nbsp; 555 018 2290</div>
<div class="a foot-l" style="left:726px;top:3597px"><span style="color:var(--orange)">✆</span>&nbsp;&nbsp; +555 01 7731</div>
<div class="a foot-l" style="left:726px;top:3628px"><span style="color:var(--orange)">✉</span>&nbsp;&nbsp; hello@aureliahair.shop</div>

<div class="a foot-h" style="left:936px;top:3488px">Follow Us on</div>
<div class="a soc" style="left:939px;background:#3b5998"></div>
<div class="a soc" style="left:979px;background:#1da1f2"></div>
<div class="a soc" style="left:1019px;background:#e24333"></div>
<div class="a" style="left:936px;top:3580px;font-size:15px;font-weight:700;color:var(--orange)">Download the App</div>
<div class="a storebtn" style="top:3610px"></div>
<div class="a storebtn" style="top:3671px"></div>

<div class="a fh" style="top:3761px">AURELIA Natural Hair</div>
<p class="a fp" style="top:3789px">Order online. All your favourite hair products from the low price online boutique with fast home delivery across many towns and cities near you, including weaves, closures, frontals, extensions and accessories. Lowest prices guaranteed on leading styles, care kits, wigs, tools and others.</p>
<div class="a fh" style="top:3855px">Shop online with the best deals &amp; offers</div>
<p class="a fp" style="top:3885px">Now Get Upto 40% Off On Everyday Essential Products Shown On The Offer Page. The range includes Bundles, Closures, Frontals, Hair Care, Wigs and Other Daily Need Products. Discount May Vary From Product To Product.</p>
<div class="a fh" style="top:3950px">Popular Brands</div>
<p class="a fp" style="top:3980px;word-spacing:6px">Alvora Ambrin Bexley Brisko Calyra Corvel Dunmore Elvan Fenwick Galden Harlow Ivara Jessop Kelby Lunaro Marlo Nessa Orlen Pavion Quenby Rellis<br>Sorva Tamsin Ulvar Wrenly Yarrow Zanel Briar Cressa Delmo Ferrin Glyde Halden</p>
<div class="a fh" style="top:4043px">Payment Method</div>
<div class="a pay" style="left:100px"></div>
<div class="a pay" style="left:151px"></div>
<div class="a pay" style="left:202px"></div>
<div class="a pay" style="left:253px"></div>
<div class="a pay" style="left:304px"></div>
<div class="a pay" style="left:364px"></div>
<div class="a pay" style="left:420px"></div>
<div class="a pay" style="left:485px"></div>
<div class="a pay" style="left:555px"></div>

<svg class="a" style="left:1136px;top:4150px" width="16" height="20" viewBox="0 0 16 20"><path d="M8 0l8 10h-5v10H5V10H0z" fill="#ff5722"/></svg>

<div class="a bottom">© 2020 AURELIA Natural Hair. All rights reserved</div>

</body>
</html>
```